Redesign of business card for Birchline Mechanical

We are looking for a new design for our business cards for Birchline Mechanical. We are a plumbing & HVAC construction company, operating on the West Coast of Canada and USA. Logo attached.
Industry/Entity Type
Construction - Plumbing & HVAC
Contact Information for Business Card
Name, address, phone numbers, email, website address
Look and feel
Each slider illustrates characteristics of the customer's brand and the style your logo design should communicate.

```html
<!DOCTYPE html>
<html lang="en">
<head>
<meta charset="utf-8">
<title>Birchline Mechanical – Business Card</title>
<link href="https://fonts.googleapis.com/css2?family=Oswald:wght@600&family=Arimo:wght@400;700&display=swap" rel="stylesheet">
<style>
  :root{
    --bg:#2b2b2d;
    --slate:#465062;
    --slate-dark:#3c4556;
    --silver:#c9d0da;
    --white:#ffffff;
    --ink:#3a3f48;
    --ink-soft:#5a606a;
  }
  *{margin:0;padding:0;box-sizing:border-box}
  html,body{width:1200px;height:875px;overflow:hidden}
  body{
    background:var(--bg);
    font-family:"Arimo",Arial,sans-serif;
    display:flex;flex-direction:column;align-items:center;justify-content:center;gap:56px;
  }
  .card{
    width:600px;height:343px;border-radius:24px;position:relative;overflow:hidden;
    box-shadow:0 18px 40px rgba(0,0,0,.45);
  }
  /* front */
  .card-front{background:var(--slate);display:flex;align-items:center;justify-content:center}
  .front-mark{display:flex;align-items:center;gap:16px}
  .front-mark .square{width:34px;height:34px;border:4px solid var(--silver)}
  .front-mark .wordmark{
    font-family:"Oswald",sans-serif;font-weight:600;font-size:34px;letter-spacing:2px;
    text-transform:uppercase;color:var(--silver);
  }
  /* back */
  .card-back{background:var(--white)}
  .name-band{
    position:absolute;left:0;top:78px;width:420px;height:98px;background:var(--slate);
    padding:22px 0 0 34px;color:var(--white);
  }
  .person-name{font-family:"Oswald",sans-serif;font-weight:600;font-size:30px;letter-spacing:1px;line-height:1}
  .person-title{font-size:15px;margin-top:8px;color:#e4e8ee}
  .brand{
    position:absolute;right:30px;top:34px;display:flex;align-items:center;gap:10px;
  }
  .brand .square{width:22px;height:22px;border:3px solid var(--slate)}
  .brand .wordmark{font-family:"Oswald",sans-serif;font-weight:600;font-size:19px;letter-spacing:1px;text-transform:uppercase;color:var(--slate)}
  .address{
    position:absolute;right:34px;top:150px;text-align:right;font-size:14px;line-height:1.4;color:var(--ink-soft);
  }
  .address .company{font-weight:700;color:var(--slate)}
  .contacts{
    position:absolute;left:34px;bottom:28px;list-style:none;font-size:14px;line-height:1.55;color:var(--ink);
  }
  .contacts li{display:flex;align-items:center;gap:10px}
  .contacts svg{width:12px;height:12px;fill:var(--slate)}
</style>
</head>
<body>
  <section class="card card-front">
    <div class="front-mark">
      <span class="square"></span>
      <span class="wordmark">Birchline Mechanical</span>
    </div>
  </section>

  <section class="card card-back">
    <div class="brand">
      <span class="square"></span>
      <span class="wordmark">Birchline Mechanical</span>
    </div>
    <div class="name-band">
      <div class="person-name">DANIEL REYES</div>
      <div class="person-title">Founder &amp; CEO</div>
    </div>
    <div class="address">
      <div class="company">Birchline Mechanical</div>
      <div>423 Street Address Here, City</div>
      <div>State &amp; Country, ZIP Code</div>
    </div>
    <ul class="contacts">
      <li><svg viewBox="0 0 24 24"><path d="M6.6 10.8a15 15 0 0 0 6.6 6.6l2.2-2.2a1 1 0 0 1 1-.25 11.4 11.4 0 0 0 3.6.6 1 1 0 0 1 1 1V20a1 1 0 0 1-1 1A17 17 0 0 1 3 4a1 1 0 0 1 1-1h3.5a1 1 0 0 1 1 1c0 1.25.2 2.45.6 3.6a1 1 0 0 1-.25 1z"/></svg>1-123-456-7890</li>
      <li><svg viewBox="0 0 24 24"><path d="M6.6 10.8a15 15 0 0 0 6.6 6.6l2.2-2.2a1 1 0 0 1 1-.25 11.4 11.4 0 0 0 3.6.6 1 1 0 0 1 1 1V20a1 1 0 0 1-1 1A17 17 0 0 1 3 4a1 1 0 0 1 1-1h3.5a1 1 0 0 1 1 1c0 1.25.2 2.45.6 3.6a1 1 0 0 1-.25 1z"/></svg>123-456-7890</li>
      <li><svg viewBox="0 0 24 24"><path d="M7 1h10a2 2 0 0 1 2 2v18a2 2 0 0 1-2 2H7a2 2 0 0 1-2-2V3a2 2 0 0 1 2-2zm0 3v15h10V4z"/></svg>123-456-7890</li>
      <li><svg viewBox="0 0 24 24"><path d="M2 5h20v14H2zm2 2v.5l8 5 8-5V7z"/></svg>info@yourwebsitehere.com</li>
      <li><svg viewBox="0 0 24 24"><circle cx="12" cy="12" r="10"/></svg>yourwebsitehere.com</li>
    </ul>
  </section>
</body>
</html>
```